Travel video blogger needs website design

I need a website designed for my new travel video blog "Roaming Sparrow". I have only just started but need a website that is fairly simple and not too busy. I have a logo which I want on it (I have attached it to this project). I also want a link to all my other social medias on the main page (vidtrekhub, Snapwell and Palnook) and my videos as well. Here is a link to my vidtrekhub page for you to look at: https://www.vidtrekhub.net/channel/QRm4tZ8pWnE2HX57YKccd31v
As I have only just started and I am still trying to find my specific niche, again I need it to be sleek and simple that I can go in and change slightly here and there. I would like these pages on the website: About Me, Videos, Social Media, Blog, Gallery, contact me. for an example I like the look of www.theroamingkinfolk.net website.

I already have the domain and I am with Harborweb with pagecraftr.org. I just want to spend my time getting better and learning about videos then trying to create a website (I am a bit of a perfectionist when I try to do something).

Target Market(s)

Young Adults (majority females) between the ages of 18 and 30 with an interest in travelling.

Industry/Entity Type

Travel Industry

Number of Pages Required

1 page

Colors

Designer to choose colors to be used in the design.

Requirements
Must have
• A like to my Snapwell, Palnook and vidtrekhub channels on the home page
• Must be a nice, simple design
• Must have my logo on the front and name "Roaming Sparrow"
Nice to have
• A nice light, bright coloured theme
Should not have
• A dark coloured theme

```html
<!DOCTYPE html>
<html lang="en">
<head>
<meta charset="UTF-8">
<title>Roaming Sparrow — Videos</title>
<link rel="stylesheet" href="https://fonts.googleapis.com/css2?family=Poppins:wght@400;500;700&display=swap">
<style>
  :root {
    --tan: #dfb984;
    --tan-text: #c69a5e;
    --page-bg: #f3f3f3;
    --white: #ffffff;
    --ink: #111111;
    --nav-ink: #333333;
    --active-bg: #f1f1f1;
  }
  * { margin: 0; padding: 0; box-sizing: border-box; }
  html, body {
    width: 1200px; height: 1200px; overflow: hidden;
    background: var(--page-bg);
    font-family: "Poppins", sans-serif;
    color: var(--ink);
  }
  .site-header {
    position: relative; height: 111px;
    background: var(--white);
    border-bottom: 1px solid var(--tan);
  }
  .nav-link {
    position: absolute; top: 0; height: 110px;
    display: flex; align-items: center;
    font-size: 13px; letter-spacing: 0.06em;
    color: var(--nav-ink); text-decoration: none; text-transform: uppercase;
  }
  .nav-link.is-active {
    background: var(--active-bg);
    border-top: 4px solid var(--tan);
    color: var(--tan-text);
    padding: 0 10px;
  }
  .brand {
    position: absolute; left: 527px; top: 0; width: 147px; height: 110px;
    background: var(--tan);
    display: flex; flex-direction: column; align-items: center; justify-content: center; gap: 10px;
    text-decoration: none;
  }
  .brand-dot {
    width: 44px; height: 44px; border-radius: 50%;
    border: 2px solid var(--ink);
  }
  .brand-name {
    font-size: 14px; font-weight: 500; color: var(--ink);
    letter-spacing: 0.02em; text-transform: uppercase;
  }
  .section-title {
    position: absolute; top: 152px; left: 0; width: 1200px;
    text-align: center; font-size: 19px; font-weight: 700;
    letter-spacing: 0.32em;
  }
  .video-grid {
    position: absolute; top: 211px; left: 93px;
    display: grid; grid-template-columns: repeat(3, 320px);
    column-gap: 26px; row-gap: 29px;
  }
  .video-card {
    width: 320px; height: 300px;
    background: var(--white);
    padding: 4px;
    box-shadow: 0 2px 4px rgba(0,0,0,0.18);
  }
  .video-thumb {
    position: relative; width: 312px; height: 225px;
    display: flex; align-items: center; justify-content: center;
  }
  .play-icon { width: 52px; height: 52px; }
  .video-caption {
    padding: 12px 8px 0;
    font-size: 15.5px; line-height: 22px;
  }
  .t-cliffs { background: linear-gradient(160deg, #b9b2a2, #7c8a7c 55%, #3f6a7a); }
  .t-pink { background: linear-gradient(180deg, #e9a9c3, #7aa3c4 55%, #3f6b7e); }
  .t-field { background: linear-gradient(180deg, #9cb8d8 0%, #5b6e3a 30%, #8b8045 100%); }
  .t-beach { background: linear-gradient(180deg, #7fb3de, #d9c7b0 55%, #e9ddd0); }
  .t-bay { background: linear-gradient(160deg, #8f9a5e, #b9b58d 50%, #d6c79f); }
  .t-selfie { background: linear-gradient(180deg, #a9b8d2, #8aa0bd 55%, #c2a88a); }
  .t-mountain { background: linear-gradient(180deg, #6e8ea8, #b7c6d1 40%, #3f4a3f); }
  .t-street { background: linear-gradient(90deg, #3d9aa4, #4a4a4a 45%, #b9bcbe); }
  .t-sunset { background: linear-gradient(180deg, #8a5a2e, #d97a2a 60%, #1e130b); }
</style>
</head>
<body>
  <header class="site-header">
    <a class="nav-link is-active" style="left:206px" href="#">About me</a>
    <a class="nav-link" style="left:314px" href="#">Videos</a>
    <a class="nav-link" style="left:392px" href="#">Social media</a>
    <a class="brand" href="#">
      <span class="brand-dot"></span>
      <span class="brand-name">Roaming Sparrow</span>
    </a>
    <a class="nav-link" style="left:727px" href="#">Blog</a>
    <a class="nav-link" style="left:795px" href="#">Gallery</a>
    <a class="nav-link" style="left:881px" href="#">Contact me</a>
  </header>

  <h1 class="section-title">AMAZING VIDEOS</h1>

  <main class="video-grid">
    <article class="video-card">
      <div class="video-thumb t-cliffs" role="img" aria-label="Traveller in a sun hat sitting on white cliffs above the sea">
        <svg class="play-icon" viewBox="0 0 52 52"><circle cx="26" cy="26" r="24" fill="none" stroke="#fff" stroke-width="2.5"/><path d="M22 18 L34 26 L22 34 Z" fill="#fff"/></svg>
      </div>
      <p class="video-caption">Welcome To The Family! (196 days until take off)</p>
    </article>
    <article class="video-card">
      <div class="video-thumb t-pink" role="img" aria-label="Traveller holding her hat on a coastal hill at pink dusk">
        <svg class="play-icon" viewBox="0 0 52 52"><circle cx="26" cy="26" r="24" fill="none" stroke="#fff" stroke-width="2.5"/><path d="M22 18 L34 26 L22 34 Z" fill="#fff"/></svg>
      </div>
      <p class="video-caption">Welcome To The Family! (196 days until take off)</p>
    </article>
    <article class="video-card">
      <div class="video-thumb t-field" role="img" aria-label="Two backpackers taking photos in a grassy field">
        <svg class="play-icon" viewBox="0 0 52 52"><circle cx="26" cy="26" r="24" fill="none" stroke="#fff" stroke-width="2.5"/><path d="M22 18 L34 26 L22 34 Z" fill="#fff"/></svg>
      </div>
      <p class="video-caption">Welcome To The Family! (196 days until take off)</p>
    </article>
    <article class="video-card">
      <div class="video-thumb t-beach" role="img" aria-label="Traveller relaxing at a colourful beach café">
        <svg class="play-icon" viewBox="0 0 52 52"><circle cx="26" cy="26" r="24" fill="none" stroke="#fff" stroke-width="2.5"/><path d="M22 18 L34 26 L22 34 Z" fill="#fff"/></svg>
      </div>
      <p class="video-caption">Welcome To The Family! (196 days until take off)</p>
    </article>
    <article class="video-card">
      <div class="video-thumb t-bay" role="img" aria-label="Two friends sitting on a wall above a sandy bay">
        <svg class="play-icon" viewBox="0 0 52 52"><circle cx="26" cy="26" r="24" fill="none" stroke="#fff" stroke-width="2.5"/><path d="M22 18 L34 26 L22 34 Z" fill="#fff"/></svg>
      </div>
      <p class="video-caption">Welcome To The Family! (196 days until take off)</p>
    </article>
    <article class="video-card">
      <div class="video-thumb t-selfie" role="img" aria-label="Traveller in a deck chair taking a selfie by the sea">
        <svg class="play-icon" viewBox="0 0 52 52"><circle cx="26" cy="26" r="24" fill="none" stroke="#fff" stroke-width="2.5"/><path d="M22 18 L34 26 L22 34 Z" fill="#fff"/></svg>
      </div>
      <p class="video-caption">Welcome To The Family! (196 days until take off)</p>
    </article>
    <article class="video-card">
      <div class="video-thumb t-mountain" role="img" aria-label="Two hikers in beanies looking over misty mountains">
        <svg class="play-icon" viewBox="0 0 52 52"><circle cx="26" cy="26" r="24" fill="none" stroke="#fff" stroke-width="2.5"/><path d="M22 18 L34 26 L22 34 Z" fill="#fff"/></svg>
      </div>
      <p class="video-caption">Welcome To The Family! (196 days until take off)</p>
    </article>
    <article class="video-card">
      <div class="video-thumb t-street" role="img" aria-label="Traveller writing postcards at a street café table">
        <svg class="play-icon" viewBox="0 0 52 52"><circle cx="26" cy="26" r="24" fill="none" stroke="#fff" stroke-width="2.5"/><path d="M22 18 L34 26 L22 34 Z" fill="#fff"/></svg>
      </div>
      <p class="video-caption">Welcome To The Family! (196 days until take off)</p>
    </article>
    <article class="video-card">
      <div class="video-thumb t-sunset" role="img" aria-label="Silhouette of a photographer and a bicycle at sunset">
        <svg class="play-icon" viewBox="0 0 52 52"><circle cx="26" cy="26" r="24" fill="none" stroke="#fff" stroke-width="2.5"/><path d="M22 18 L34 26 L22 34 Z" fill="#fff"/></svg>
      </div>
      <p class="video-caption">Welcome To The Family! (196 days until take off)</p>
    </article>
  </main>
</body>
</html>
```